wig manufacturer
I would like something very upscale.highend looking
maybe mat chrome card with shiney chrome
or something like the Quince business card very clean and simple white with the logo in silver
Target Market(s)
upscale women
Industry/Entity Type
Business
Contact Information for Business Card
OUR LOGO
company name:Rosamund Wigs
48E92Avenue Harold Pinsett
New York,N.Y 10018
Tel:212-5550148
1800-5550193
email:tressline@mailbox.example
website:Rosamundwigs.example

```html
<!DOCTYPE html>
<html lang="en">
<head>
<meta charset="utf-8">
<title>Rosamund Wigs – Business Card</title>
<link rel="stylesheet" href="https://fonts.googleapis.com/css2?family=Cormorant+Garamond:wght@500&family=Source+Sans+3:wght@300;400&display=swap">
<style>
  :root {
    --backdrop: #ececed;
    --card: #ffffff;
    --brand-blue: #1c5aa5;
    --ink: #3d3d3d;
    --ink-strong: #2b2b2b;
    --rule: #6f6f6f;
    --silver: #d9dadc;
  }
  * { box-sizing: border-box; margin: 0; padding: 0; }
  html, body {
    width: 1200px; height: 1000px; overflow: hidden;
    background: var(--backdrop);
  }
  .business-card {
    position: absolute; left: 275px; top: 315px;
    width: 650px; height: 372px;
    background: var(--card);
    font-family: "Source Sans 3", "Myriad Pro", sans-serif;
    font-weight: 300;
    color: var(--ink);
  }
  .tagline {
    position: absolute; top: 27px; left: 0; width: 100%;
    text-align: center;
    font-family: "Cormorant Garamond", Georgia, serif;
    font-size: 19px; letter-spacing: 0.7px; color: var(--ink);
  }
  .brand-mark {
    position: absolute; left: 93px; top: 94px;
    width: 120px;
  }
  .brand-mark__name {
    font-size: 20px; font-weight: 300; color: var(--ink);
    line-height: 1;
  }
  .brand-mark__square {
    margin-top: 14px; width: 100px; height: 124px;
    background: var(--silver);
  }
  .company {
    position: absolute; left: 280px; top: 98px;
  }
  .company__name {
    font-size: 43px; font-weight: 300; color: var(--brand-blue);
    line-height: 1.1; margin-bottom: 4px;
  }
  .company__line {
    font-size: 23px; line-height: 30px; color: var(--ink);
  }
  .company__web {
    font-size: 24px; font-weight: 400; line-height: 30px; color: var(--ink-strong);
  }
  .contact-rule {
    position: absolute; left: 44px; top: 310px;
    width: 562px; height: 1px; background: var(--rule);
  }
  .contact-row {
    position: absolute; left: 56px; top: 316px; width: 552px;
    display: flex; justify-content: space-between; align-items: center;
    font-size: 21px; color: var(--ink);
  }
  .contact-item { display: flex; align-items: center; gap: 6px; white-space: nowrap; }
  .contact-item svg { fill: var(--brand-blue); display: block; }
</style>
</head>
<body>
  <main class="business-card">
    <p class="tagline">“THIS IS NOT YOUR MOTHER ROSAMUND WIG”</p>

    <div class="brand-mark">
      <div class="brand-mark__name">Rosamund</div>
      <div class="brand-mark__square"></div>
    </div>

    <section class="company">
      <h1 class="company__name">Rosamund Wigs</h1>
      <p class="company__line">48E92Avenue Harold Pinsett</p>
      <p class="company__line">New York,N.Y 10018</p>
      <p class="company__web">rosamundwigs.example</p>
    </section>

    <div class="contact-rule"></div>

    <div class="contact-row">
      <span class="contact-item">
        <svg width="12" height="22" viewBox="0 0 12 22" aria-hidden="true">
          <rect x="8" y="0" width="2" height="5"/>
          <path d="M1 5h10a1 1 0 0 1 1 1v15a1 1 0 0 1-1 1H1a1 1 0 0 1-1-1V6a1 1 0 0 1 1-1zm1 2v5h8V7z"/>
        </svg>
        212-5550148 · 1800-5550193
      </span>
      <span class="contact-item">
        <svg width="24" height="16" viewBox="0 0 24 16" aria-hidden="true">
          <path d="M0 0h24v16H0z" fill="var(--brand-blue)"/>
          <path d="M1.5 1.5l10.5 8.5 10.5-8.5" stroke="#fff" stroke-width="1.4" fill="none"/>
        </svg>
        tressline@mailbox.example
      </span>
    </div>
  </main>
</body>
</html>
```